【業務の内容】
建物(鉄筋(鉄骨)コンクリート躯体)の寿命が、あとどれくらい
残っているのか(=寿命)を評価する業務

【なぜこの業務が必要か】
・いまお住まいのマンションの将来計画を考えるために重要な基礎資料
例えば
・「建物寿命は、あと50年以上あるので、しっかりと設備も改修しよう」
・「建物寿命は、あと50年以上あるので、耐震補強を考えよう」
・「建物寿命が20年程度しか残っていないから、延命のための改修をしよう」
・「建物寿命が20年程度しか残っていないから、建替えの検討をしよう」
・残存寿命が長いなら、耐震補強や給排水設備の改修、共用部のリニューアル等を
実施する価値がある、と判断できる

【この業務を推す背景】
・築30年、40年を超える高経年マンションが増えてきている
・首都圏では大地震の確率が30年以内に70%と言われており。1981年以前の旧耐震
基準の建物は、すでに築40年を超えており、耐震補強工事を行うか、建替えるかの
選択を迫られている

【業務の費用(目安・税別)】 ※あくまでも目安
・1棟当たり 基本料金300,000+コア抜き50,000/ヶ所(1フロアあたり1ヶ所)

例)5階建て1棟のマンションの場合
基本料金300,000+(50,000×5ヶ所)=550,000(税別)
【訴求したい事】
・建物の寿命評価に特化しているので、耐震診断等と比べて比較的
安価に実施できる
・短期間で結果が分かる(着手後およそ1か月程度)
・これからマンションにどれだけ維持修繕や改良などの投資するかという
検討をする際の客観的裏付けのある基礎資料になる
・耐用年数は「集合住宅躯体の長期保全評価指針・同付録」(日本建築
学会)の示す算定式を使って算出する

【特に注意・留意すべき事象】
・「寿命が長い」=「安全」ではない
建物耐用年数が長くても、現在の耐震性能基準に達していなければ大地震で
大破・倒壊の危険性がある。躯体寿命と建物の安全性は全く別物
・建物の寿命と設備(給排水管や電気設備など)の寿命は別物
株式会社環創プラン 本社
〒150-0074
東京都渋谷区桜見台7-13-6朝陽ビル
TEL:03-6928-4171(代)
FAX:03-6928-4178

西日本支社
大阪事務所
〒530-0086
大阪府大阪市北区松風町 6-3-18 青葉セントラルビル
TEL:06-6384-2051
FAX:06-6384-2052

西日本支社
広島事務所
〒730-0094
広島県広島市中区千草通3-8-12浜辺ビル5F
TEL:082-517-6820
FAX:082-517-6829
A4
両面
赤系、緑系、水色系
• 高解像度JPG (.jpg)
• イラストレーター形式 (.ai)
使用可能な画像、図(こちらもチラシ作成上に入れてほしいがわかりやすくいじってもらってOKです)、会社ロゴ等全て添付します。

業界関係者ではなく、一般のかた(いわゆる「素人」)が、パッとみてどう感じるだろうか、という
目線で選定しました。
・あまり小難しい印象は与えず、明快なデザイン
・「マンション販売のチラシ」や「水道修理業者」と勘違いされない
というようなところで差がありました。

はじめてこのワークバザールを利用したのですが、このように色々なご提案をいただき、
正直、驚き(もちろん嬉しい方です)でした。
やはりプロにお任せするだけのことがあると痛感し、
我々の業務も同じような驚きをお客様にお届けできるように心がけたいと思います。

この度はご提案いただきまして、誠にありがとうございました。

```html
<!DOCTYPE html>
<html lang="ja">
<head>
<meta charset="utf-8">
<title>マンション向け 建物耐用年数評価のご案内</title>
<link rel="stylesheet" href="https://fonts.googleapis.com/css2?family=Noto+Sans+JP:wght@400;500;700;900&display=swap">
<style>
:root{
  --red:#d8261e;
  --orange:#f0911c;
  --teal:#0f8f86;
  --teal-dark:#0a6f68;
  --ink:#222;
  --gray:#9ea3a6;
  --paper:#ffffff;
}
*{margin:0;padding:0;box-sizing:border-box}
html,body{width:849px;height:1200px;overflow:hidden;background:#fff}
body{font-family:"Noto Sans JP",sans-serif;color:var(--ink);position:relative}
.hero-photo{position:absolute;left:0;top:0;width:849px;height:590px;
  background:linear-gradient(180deg,#8c9195 0%,#c4c8ca 45%,#e6e8e9 80%,#fff 100%)}
.vertical{position:absolute;writing-mode:vertical-rl;font-weight:900;color:rgba(255,255,255,.55);letter-spacing:6px}
.v-left1{left:14px;top:10px;font-size:46px}
.v-left2{left:62px;top:190px;font-size:46px;color:rgba(255,255,255,.4)}
.v-right{right:14px;top:20px;font-size:46px}
.badge{position:absolute;left:236px;top:16px;width:378px;height:48px;border-radius:24px;background:var(--orange);
  color:#fff;font-size:30px;font-weight:900;text-align:center;line-height:48px;letter-spacing:2px}
.title{position:absolute;left:0;width:849px;text-align:center;font-weight:900}
.title span{background:#fff;padding:0 10px}
.title-main{top:70px;font-size:58px;color:var(--red);line-height:72px}
.title-sub{top:146px;font-size:50px;line-height:62px}
.lead{position:absolute;left:0;top:218px;width:849px;text-align:center;font-size:17px;font-weight:700;line-height:28px}
.lead span{background:rgba(255,255,255,.85);padding:0 6px}
.key{position:absolute;left:0;top:282px;width:849px;text-align:center;font-size:19px;font-weight:900;color:var(--teal-dark);line-height:28px}
.key span{background:rgba(255,255,255,.85);padding:0 6px}
.quotes{position:absolute;left:150px;top:346px;width:550px;list-style:none}
.quotes li{position:relative;height:27px;margin-bottom:6px;background:#fff;border:2px solid var(--orange);
  color:var(--red);font-size:15px;font-weight:700;line-height:23px;padding-left:20px}
.quotes li::before,.quotes li::after{content:"";position:absolute;top:-2px;width:10px;height:27px;background:var(--orange)}
.quotes li::before{left:-12px}.quotes li::after{right:-12px}
.note{position:absolute;left:130px;top:484px;width:590px;font-size:13px;line-height:21px;font-weight:500}
.note span{background:rgba(255,255,255,.8)}
.row{position:absolute;left:22px;width:805px;display:flex;gap:16px}
.label{width:150px;flex:none;background:var(--teal);color:#fff;font-size:14px;font-weight:700;line-height:21px;padding:10px 10px}
.label small{display:block;font-size:10px;font-weight:400}
.body{flex:1;font-size:13px;line-height:21px}
.body ul{list-style:none}
.body li{padding-left:1em;text-indent:-1em}
.row-bg{top:600px;height:100px}
.row-cost{top:715px;height:115px}
.row-method{top:845px;height:280px}
.example{margin-top:8px;border:1.5px solid var(--teal);padding:6px 12px;font-size:13px}
.example em{font-style:normal;display:block;padding-left:28px;font-weight:700}
.divider{position:absolute;left:22px;width:805px;height:1px;background:var(--gray)}
.steps{position:absolute;left:22px;top:900px;width:805px;display:flex;gap:14px}
.step{flex:1}
.step-head{display:flex;align-items:center;gap:8px;font-size:14px;font-weight:700;margin-bottom:6px}
.step-num{width:22px;height:22px;border-radius:50%;background:var(--orange);color:#fff;text-align:center;line-height:22px;font-size:13px}
.step-photo{height:200px;background:linear-gradient(160deg,#bfc6c4,#8e9896)}
.foot{position:absolute;left:0;bottom:0;width:849px;height:40px;background:var(--teal)}
</style>
</head>
<body>
<div class="hero-photo" role="img" aria-label="マンションが立ち並ぶ街並みのモノクロ写真"></div>
<div class="vertical v-left1">建物寿命</div>
<div class="vertical v-left2">耐震補強</div>
<div class="vertical v-right">首都圏大地震</div>

<div class="badge">マンション向け</div>
<h1 class="title title-main"><span>建物耐用年数評価</span></h1>
<p class="title title-sub"><span>のご案内</span></p>

<p class="lead"><span>建物（鉄筋（鉄骨）コンクリート躯体）の寿命が、</span><br><span>あとどれくらい残っているのか（＝寿命）を評価する調査です。</span></p>
<p class="key"><span>いまお住まいのマンションの将来計画を考えるために</span><br><span>重要な基礎資料となります。</span></p>

<ul class="quotes">
  <li>「建物寿命は、あと50年以上あるので、しっかりと設備も改修しよう」</li>
  <li>「建物寿命は、あと50年以上あるので、耐震補強を考えよう」</li>
  <li>「建物寿命が20年程度しか残っていないから、延命のための改修をしよう」</li>
  <li>「建物寿命が20年程度しか残っていないから、建替えの検討をしよう」</li>
</ul>

<p class="note"><span>残存寿命が長いなら、耐震補強や給排水設備の改修、共用部のリニューアル等を</span><br><span>実施する価値がある、と判断できます。</span></p>

<section class="row row-bg">
  <h2 class="label">建物耐用年数評価が<br>必要とされる背景</h2>
  <div class="body"><ul>
    <li>● 築30年、40年を超える高経年マンションが増えてきています。</li>
    <li>● 首都圏では大地震の確率が30年以内に70%と言われており、1981年以前の旧耐震基準の建物は、すでに築40年を超えており、耐震補強工事を行うか、建替えるかの選択を迫られています。</li>
  </ul></div>
</section>
<div class="divider" style="top:707px"></div>

<section class="row row-cost">
  <h2 class="label">調査費用の目安<small>※あくまでも目安です</small></h2>
  <div class="body">
    <p>● 1棟当たり　基本料金300,000＋コア抜き50,000／ヶ所（1フロアあたり1ヶ所）</p>
    <p class="example">例）5階建て1棟のマンションの場合<em>基本料金300,000＋（50,000×5ヶ所）＝550,000（税別）</em></p>
  </div>
</section>
<div class="divider" style="top:837px"></div>

<section class="row row-method">
  <h2 class="label">調査方法</h2>
  <div class="body"><p>建物のコア抜き（壁に円筒形の穴を空ける）により検体を取り、その検体の中性化の進行具合や圧縮強度を調べることで建物のコンクリート躯体寿命を評価します。</p></div>
</section>

<div class="steps">
  <div class="step"><p class="step-head"><span class="step-num">1</span>コア抜き作業</p><div class="step-photo" role="img" aria-label="作業員が壁のコア抜きを行う写真"></div></div>
  <div class="step"><p class="step-head"><span class="step-num">2</span>空いた穴の補修</p><div class="step-photo" role="img" aria-label="コア抜き後の穴を補修した壁の写真"></div></div>
  <div class="step"><p class="step-head"><span class="step-num">3</span>コアの試験</p><div class="step-photo" role="img" aria-label="採取したコンクリートコアを試験する写真"></div></div>
</div>

<div class="foot"></div>
</body>
</html>
```